Kestrow Fire Services Pty Ltd

We need business cards for a company based in Perth, we install, service and maintain fire equipment.
On the front we want a great design with our logo and a small spot for our full company name, general company email address and office number. On the back we need space for our name, title, mobile number and email address on the back.

Target Market(s)

Facility managers and commercial/industrial building owners/occupiers.

Contact Information for Business Card

Font styles to use
Sans Serif

Requirements
Must have
• Please only submit 5 of your best samples.
Darker tones are preferred.
Nice to have
• We want to use, black, red and grey. Keep it modern and clean.
I've attached the company logo and a sample of a boarder we use on our emergency plans.
Should not have
• No preference. Let the designer choose.

```html
<!DOCTYPE html>
<html lang="en">
<head>
<meta charset="utf-8">
<title>Kestrow Fire Services – Business Card</title>
<link rel="stylesheet" href="https://fonts.googleapis.com/css2?family=Arimo:wght@400;700&family=Poppins:wght@400;500&display=swap">
<style>
  :root {
    --backdrop: #d9d6d1;
    --card-black: #000000;
    --card-grey: #656b6d;
    --fire-red: #e3232a;
    --ink-white: #ffffff;
    --ink-black: #0b0b0b;
    --rule-dark: #2a2c2d;
  }
  * { margin: 0; padding: 0; box-sizing: border-box; }
  html, body { width: 900px; height: 1200px; overflow: hidden; }
  body {
    background: var(--backdrop);
    position: relative;
    font-family: "Arimo", Arial, sans-serif;
  }
  .card {
    position: absolute;
    left: 80px;
    width: 735px;
    height: 430px;
    border-radius: 22px;
    overflow: hidden;
  }
  .card--personal { top: 127px; background: var(--card-black); }
  .card--company { top: 645px; background: var(--card-grey); }

  .brand-name {
    position: absolute;
    right: 42px;
    font-family: "Arimo", Arial, sans-serif;
    font-weight: 700;
    font-size: 46px;
    letter-spacing: 0.5px;
    line-height: 1;
  }
  .card--personal .brand-name { top: 100px; color: var(--fire-red); }
  .card--company .brand-name { top: 98px; color: var(--ink-black); }

  .legal-name {
    position: absolute;
    right: 42px;
    top: 177px;
    font-weight: 700;
    font-size: 10.5px;
    color: var(--ink-black);
    letter-spacing: 0.2px;
  }

  .accent-bar { position: absolute; left: 0; height: 15px; width: 164px; }
  .card--personal .accent-bar { top: 307px; background: var(--fire-red); }
  .card--company .accent-bar { top: 313px; width: 161px; background: var(--ink-black); }

  .rule { position: absolute; left: 185px; right: 0; height: 1.5px; }
  .card--personal .rule { top: 320px; background: var(--fire-red); }
  .card--company .rule { top: 326px; left: 183px; background: var(--rule-dark); }

  .person {
    position: absolute;
    left: 44px;
    top: 348px;
    font-weight: 700;
  }
  .person__name { font-size: 17px; color: var(--ink-white); line-height: 20px; letter-spacing: 0.3px; }
  .person__title { font-size: 13px; color: var(--fire-red); line-height: 18px; letter-spacing: 0.6px; }

  .office-label {
    position: absolute;
    right: 574px;
    top: 347px;
    font-weight: 700;
    font-size: 16px;
    color: var(--ink-black);
    letter-spacing: 0.3px;
  }

  .contacts { position: absolute; list-style: none; }
  .contacts li { display: flex; align-items: center; height: 23px; }
  .contacts svg { flex: none; margin-right: 8px; }
  .card--personal .contacts { left: 184px; top: 346px; color: var(--ink-white); font-size: 16px; }
  .card--company .contacts {
    left: 181px; top: 345px; color: var(--ink-black);
    font-family: "Poppins", Arial, sans-serif; font-size: 15.5px; line-height: 1;
  }
  .card--company .contacts li { height: 26px; }
</style>
</head>
<body>

<section class="card card--personal">
  <div class="brand-name">KESTROW</div>
  <div class="accent-bar"></div>
  <div class="rule"></div>
  <div class="person">
    <div class="person__name">DANIEL MARSH</div>
    <div class="person__title">MANAGER</div>
  </div>
  <ul class="contacts">
    <li>
      <svg width="14" height="18" viewBox="0 0 14 18" aria-hidden="true">
        <rect x="2" y="1" width="10" height="16" rx="2" fill="none" stroke="var(--fire-red)" stroke-width="2"/>
        <rect x="5" y="13" width="4" height="1.6" fill="var(--fire-red)"/>
      </svg>
      0133-2241-5082
    </li>
    <li>
      <svg width="15" height="12" viewBox="0 0 15 12" aria-hidden="true">
        <rect x="0" y="1" width="15" height="10" fill="var(--fire-red)"/>
        <path d="M0 1 L7.5 7 L15 1" fill="none" stroke="#000" stroke-width="1.3"/>
      </svg>
      daniel@kestrowfire.com.au
    </li>
  </ul>
</section>

<section class="card card--company">
  <div class="brand-name">KESTROW</div>
  <div class="legal-name">KESTROW FIRE SERVICES PTY LTD</div>
  <div class="accent-bar"></div>
  <div class="rule"></div>
  <div class="office-label">OFFICE</div>
  <ul class="contacts">
    <li>
      <svg width="16" height="16" viewBox="0 0 24 24" aria-hidden="true">
        <path fill="var(--ink-black)" d="M6.6 10.8a15.1 15.1 0 0 0 6.6 6.6l2.2-2.2a1 1 0 0 1 1-.25 11.4 11.4 0 0 0 3.6.57 1 1 0 0 1 1 1V20a1 1 0 0 1-1 1A17 17 0 0 1 3 4a1 1 0 0 1 1-1h3.5a1 1 0 0 1 1 1c0 1.25.2 2.45.57 3.57a1 1 0 0 1-.25 1z"/>
      </svg>
      0148 3306 7719
    </li>
    <li>
      <svg width="16" height="12" viewBox="0 0 16 12" aria-hidden="true">
        <rect x="0" y="0.5" width="16" height="11" fill="var(--ink-black)"/>
        <path d="M0 0.5 L8 7 L16 0.5" fill="none" stroke="var(--card-grey)" stroke-width="1.3"/>
      </svg>
      info@kestrowfire.com.au
    </li>
  </ul>
</section>

</body>
</html>
```